Trucking Company Website Design

We are working with a Trucking company in California. They provide trucking services for dirt, gravel, landscape bark, and landscape materials.

As you might imagine, there are no websites we could find for inspiration for trucking companies.

Thank you for taking the time to consider designing a website for us. We are web developers based in Stockton, CA, USA. Most of our projects go through the same process. Understanding this process may help you win a project with us. We custom-code all of our websites in-house. We don’t have any requirements as to what tools you use for your design, but we ask that you follow these guidelines.

IMAGES:
If you use any images or icons in the design, we ask that you have a link to the asset so we can purchase the image/icon. Most of the designs we submit do not have the customer’s images on them unless they have some great images. Be creative; show us the feeling you are trying to portray with your image choices. Use any royalty-free site you choose. We subscribe to Veltro and mainly use their images, but we can purchase images outside of Veltro. PLEASE NOTE: we will not submit designs to clients with watermarks on the images.

FONTS:
We ask that you identify the fonts you’re using in the design. This can be done in a message if you want. We typically use Plimsa Fonts and Veltro Fonts.

CONTENT:
We're always open to different content and ideas. We often submit designs with stock images so the client can see our vision. We typically take pictures after the website launch to use their images with our vision. Lorem Ipsum is fine for paragraphs, but we ask that you make the Headers with correct English. We want to be able to show the vision and identify the sections of the website.

INSPIRATION:
We typically add a couple of links in the brief of websites we like to help you get started in your design.

REVISIONS:
We do not often ask for revisions of the designs unless we see something in the design that may not appeal to the client. If there are slight changes that we want to make, we do that in the development process.

FEEDBACK:
We rarely give feedback on designs during the design process. We are working on many website projects and do not have the time to provide feedback. We usually respond if your request is well thought out and asks specific questions, but a note asking “feedback, please” usually goes unanswered.

```html
<!DOCTYPE html>
<html lang="en">
<head>
<meta charset="utf-8">
<title>Ridgeline Haulage – Trucking</title>
<link href="https://fonts.googleapis.com/css2?family=Roboto:wght@400;500;700&display=swap" rel="stylesheet">
<style>
:root{
  --blue:#0a9ddc;
  --blue-dark:#0787c0;
  --red:#f42f45;
  --ink:#1b1b1b;
  --grey:#6c6c6c;
  --line:#d8d8d8;
  --white:#fff;
}
*{box-sizing:border-box;margin:0;padding:0}
html,body{width:1200px;height:3522px;overflow:hidden}
body{font-family:'Roboto',sans-serif;color:var(--ink);background:var(--white);position:relative}
.abs{position:absolute}

/* header */
.header{position:absolute;left:0;top:0;width:1200px;height:98px;background:var(--white)}
.header-band{position:absolute;left:336px;top:0;width:864px;height:98px;background:var(--blue);clip-path:polygon(0 0,100% 0,100% 100%,0 100%,22px 50%)}
.header-rule{position:absolute;left:355px;top:48px;width:845px;height:2px;background:rgba(255,255,255,.55)}
.brand{position:absolute;display:flex;align-items:center;gap:8px;font-weight:700;color:var(--blue);font-size:19px;letter-spacing:.3px;white-space:nowrap;z-index:2}
.brand-square{width:14px;height:14px;background:var(--red);flex:none}
.phone{position:absolute;right:118px;top:10px;display:flex;align-items:center;gap:8px;color:var(--white);font-weight:700;font-size:19px}
.nav{position:absolute;top:63px;left:0;width:1200px;height:20px}
.nav a{position:absolute;color:var(--white);text-decoration:none;font-weight:700;font-size:15px}

/* hero */
.hero{position:absolute;left:0;top:98px;width:1200px;height:585px;background:linear-gradient(180deg,#3d4450 0%,#6a6258 38%,#b98a4a 58%,#5a4a35 78%,#3a3228 100%)}
.hero-title{position:absolute;top:58px;left:0;width:1200px;text-align:center;color:var(--white);font-weight:700;font-size:46px;line-height:56px}
.btn{position:absolute;display:flex;align-items:center;justify-content:center;font-weight:700;color:var(--white);background:var(--blue);clip-path:polygon(14px 0,100% 0,100% 100%,14px 100%,0 50%)}
.btn::after{content:"";position:absolute;right:0;top:0;width:30px;height:100%;background:var(--red)}
.btn span{position:relative;margin-right:26px}

/* section headings */
.heading{position:absolute;font-weight:700;line-height:1}
.heading .kicker{display:block;color:var(--blue);font-size:23px}
.heading .main{display:block;font-size:37px;white-space:nowrap}
.heading .mark{position:absolute;width:22px;height:22px;background:var(--red)}

/* services */
.card{position:absolute;top:850px;width:219px;height:323px;border:1px solid var(--line);border-radius:8px;overflow:hidden;background:var(--white);text-align:center}
.card-img{height:168px}
.card h3{margin-top:16px;font-size:17px;font-weight:500;color:#333}
.card p{margin:15px auto 0;width:180px;font-size:12px;line-height:15px;color:#444}
.card .btn{left:54px;top:278px;width:110px;height:28px;font-size:9px}
.card .btn::after{width:22px}
.card .btn span{margin-right:20px}

/* about */
.about{position:absolute;left:0;top:1286px;width:1200px;height:553px;background:var(--blue)}
.about p{position:absolute;left:615px;top:193px;width:464px;text-align:right;color:var(--white);font-size:13.6px;line-height:18.8px;font-weight:400}
.btn-outline{position:absolute;left:891px;top:393px;width:185px;height:50px;display:flex;align-items:center;justify-content:center;color:var(--white);font-weight:700;font-size:17px}
.btn-outline svg{position:absolute;left:0;top:0}
.btn-outline span{position:relative;margin-right:28px}

/* blog */
.blog-feature{position:absolute;left:120px;top:2094px;width:432px;height:388px;border-radius:6px;overflow:hidden;background:linear-gradient(180deg,#8a8a86 0%,#b76040 45%,#3a3a38 75%,#101010 100%)}
.blog-feature h3{position:absolute;left:36px;bottom:36px;width:370px;color:var(--white);font-size:22px;font-weight:500;line-height:24px}
.blog-thumb{position:absolute;left:575px;width:211px;height:182px;border-radius:6px}
.blog-item{position:absolute;left:809px;width:280px}
.blog-item h4{font-size:22px;font-weight:500;line-height:23px;color:var(--ink)}
.blog-item p{margin-top:10px;font-size:13.5px;line-height:20px;color:var(--grey)}
.blog-item time{display:block;margin-top:8px;color:var(--red);font-weight:700;font-size:16.5px}

/* contact */
.contact{position:absolute;left:0;top:2612px;width:1200px;height:523px;background:var(--red)}
.contact .heading{color:var(--white)}
.contact .heading .kicker{color:var(--white)}
.field{position:absolute;background:var(--white);color:#777;font-size:14px;padding:12px 18px}
.submit{position:absolute;left:275px;top:361px;width:179px;height:48px;font-size:16px}

/* footer */
.footer{position:absolute;left:0;top:3135px;width:1200px;height:387px;background:var(--white)}
.footer-about{position:absolute;left:154px;top:193px;width:230px;font-size:13px;line-height:17px;color:#999}
.footer-col{position:absolute;top:89px}
.footer-col h5{color:var(--red);font-size:20px;font-weight:500;margin-bottom:12px}
.footer-col li{list-style:none;font-size:14px;color:#555;height:31px}
.contact-row{position:absolute;left:768px;display:flex;gap:12px;font-size:14px;line-height:22px;color:#555}
.contact-row .icon{width:34px;height:34px;flex:none;background:var(--blue);display:flex;align-items:center;justify-content:center}
.footer-rule{position:absolute;left:154px;top:314px;width:885px;height:1px;background:var(--line)}
.copyright{position:absolute;top:341px;left:0;width:1200px;text-align:center;font-size:14px;color:#555}
</style>
</head>
<body>

<header class="header">
  <div class="header-band"></div>
  <div class="header-rule"></div>
  <div class="brand" style="left:106px;top:37px"><span>RIDGELINE HAULAGE</span><span class="brand-square"></span></div>
  <div class="phone">
    <svg width="22" height="22" viewBox="0 0 22 22"><rect width="22" height="22" rx="5" fill="#fff"/><path d="M7 5l3 3-1.5 2a9 9 0 0 0 3.5 3.5l2-1.5 3 3-2 2C10 17 5 12 5 7z" fill="#0a9ddc"/></svg>
    <span>5550142298</span>
  </div>
  <nav class="nav">
    <a style="left:553px">Home</a>
    <a style="left:638px">About us</a>
    <a style="left:743px">Trucking</a>
    <a style="left:847px">Services</a>
    <a style="left:950px">Blog</a>
    <a style="left:1026px">Contact</a>
  </nav>
</header>

<section class="hero" role="img" aria-label="Dump truck driving down a dusty rural road at sunset">
  <h1 class="hero-title">WELCOME TO<br>RIDGELINE HAULAGE</h1>
  <a class="btn" style="left:508px;top:184px;width:184px;height:49px;font-size:16px"><span>GET A QUOTE</span></a>
</section>

<div class="heading" style="left:514px;top:740px;text-align:right;width:172px">
  <span class="kicker">OUR</span><span class="main">SERVICES</span>
  <span class="mark" style="left:184px;top:14px"></span>
</div>

<article class="card" style="left:120px">
  <div class="card-img" role="img" aria-label="Excavator unloading dirt" style="background:linear-gradient(160deg,#9ea3a8,#6c6d68 55%,#a69a86)"></div>
  <h3>DIRT</h3>
  <p>Lorem ipsum dolor sit amet, consectetur adip iscing elit, sed do eiusmod tempor</p>
  <a class="btn"><span>READ MORE</span></a>
</article>
<article class="card" style="left:367px">
  <div class="card-img" role="img" aria-label="Orange dump truck with a load of gravel" style="background:linear-gradient(160deg,#d8dcdf,#c46a36 55%,#4a4a4a)"></div>
  <h3>GRAVEL</h3>
  <p>Lorem ipsum dolor sit amet, consectetur adip iscing elit, sed do eiusmod tempor</p>
  <a class="btn"><span>READ MORE</span></a>
</article>
<article class="card" style="left:614px">
  <div class="card-img" role="img" aria-label="Road rollers working on a new surface" style="background:linear-gradient(180deg,#7fa7c8,#e0a060 45%,#3a3a3a)"></div>
  <h3>LANDSCAPE BARK</h3>
  <p>Lorem ipsum dolor sit amet, consectetur adip iscing elit, sed do eiusmod tempor</p>
  <a class="btn"><span>READ MORE</span></a>
</article>
<article class="card" style="left:861px">
  <div class="card-img" role="img" aria-label="Piles of crushed stone and sand" style="background:linear-gradient(150deg,#9a9a98,#c2bfb8 55%,#c99a6a)"></div>
  <h3>LANDSCAPE MATERIALS</h3>
  <p>Lorem ipsum dolor sit amet, consectetur adip iscing elit, sed do eiusmod tempor</p>
  <a class="btn"><span>READ MORE</span></a>
</article>

<section class="about">
  <div class="abs" style="left:139px;top:47px;width:151px;height:232px;background:var(--red);border-radius:10px"></div>
  <div class="abs" role="img" aria-label="Excavator loading a dump truck at a quarry" style="left:168px;top:74px;width:366px;height:398px;border-radius:8px;background:linear-gradient(170deg,#e8ecef,#9aa3ab 45%,#5a5c5d 70%,#b7a893)"></div>
  <div class="heading" style="left:600px;top:118px;width:428px;text-align:right;color:var(--white)">
    <span class="kicker" style="color:var(--white)">ABOUT</span><span class="main">RIDGELINE HAULAGE</span>
    <span class="mark" style="left:440px;top:14px"></span>
  </div>
  <p>Lorem ipsum dolor sit amet, consectetur adipiscing elit, sed do eiusmod tempor incididunt ut labore et dolore magna aliqua. Quis ipsum susp endisse ultrices gravida. Risus commodo viverra maecenas Lorem ipsum dolor sit amet, consectetur adipiscing elit, sed do eiusmod tempor incid idunt ut labore et dolore magna aliqua. Quis ipsum suspendisse ultrices gravida. Risus commodo viverra maecenas accumsan lacus vel facilisis. accumsan lscing elit, sed do eiusmod tempor incid idunt ut labore et dolore magna aliqua. Quis ipsum suspendisse ultrices gravida. Risus commodo viverra maecenas accumsan lacacus vel facilisis.</p>
  <a class="btn-outline">
    <svg width="185" height="50" viewBox="0 0 185 50"><polygon points="16,1 184,1 184,49 16,49 1,25" fill="none" stroke="#fff" stroke-width="2"/><rect x="152" y="1" width="32" height="48" fill="#f42f45"/></svg>
    <span>READ MORE</span>
  </a>
</section>

<div class="heading" style="left:480px;top:1972px;width:236px;text-align:right">
  <span class="kicker">OUR</span><span class="main">LATEST BLOG</span>
  <span class="mark" style="left:248px;top:14px"></span>
</div>

<article class="blog-feature" role="img" aria-label="Orange dump truck parked under a cloudy sky">
  <h3>Lorem ipsum dolor loesit ame cons ectetur adipiscing elitsed</h3>
</article>
<div class="blog-thumb" role="img" aria-label="Yellow dump truck tipping its load" style="top:2096px;background:linear-gradient(170deg,#c9d6e2,#d8c23a 45%,#b49a6a)"></div>
<article class="blog-item" style="top:2103px">
  <h4>Lorem ipsum dolor loesit amet, consectetur</h4>
  <p>Lorem ipsum dolor sit amet, consectetur adipiscing elit, sed do eiusmod tempor inc idi dunt ut labore et dolore magaliqua.</p>
  <time>June 20 2023</time>
</article>
<div class="blog-thumb" role="img" aria-label="Dump truck unloading sand under a blue sky" style="top:2299px;background:linear-gradient(170deg,#4f8ed0,#9a8a70 50%,#c9a977)"></div>
<article class="blog-item" style="top:2306px">
  <h4>Lorem ipsum dolor loesit amet, consectetur</h4>
  <p>Lorem ipsum dolor sit amet, consectetur adipiscing elit, sed do eiusmod tempor inc idi dunt ut labore et dolore magaliqua.</p>
  <time>June 20 2023</time>
</article>

<section class="contact">
  <div class="heading" style="left:200px;top:90px;width:255px;text-align:right">
    <span class="kicker">CONTACT</span><span class="main">GET IN TOUCH</span>
    <span class="mark" style="left:268px;top:14px;background:var(--white)"></span>
  </div>
  <div class="field" style="left:119px;top:178px;width:251px;height:44px">First Name</div>
  <div class="field" style="left:381px;top:178px;width:253px;height:44px">Last Name</div>
  <div class="field" style="left:119px;top:237px;width:251px;height:42px">Phone</div>
  <div class="field" style="left:381px;top:237px;width:253px;height:42px">Email</div>
  <div class="field" style="left:119px;top:296px;width:515px;height:86px">Messgae</div>
  <a class="btn submit"><span>SUBMIT NOW</span></a>
  <div class="abs" style="left:695px;top:73px;width:382px;height:382px;border-radius:50%;border:2px solid var(--white)"></div>
  <div class="abs" role="img" aria-label="White dump truck raising a yellow bed" style="left:711px;top:89px;width:350px;height:350px;border-radius:50%;background:linear-gradient(160deg,#6fa6d8,#e0c040 40%,#e8e8e8 60%,#7a7060)"></div>
</section>

<footer class="footer">
  <div class="brand" style="left:154px;top:108px"><span>RIDGELINE HAULAGE</span><span class="brand-square"></span></div>
  <p class="footer-about">Lorem ipsum dolor sit amet lore consectetur adipiscing elit, sed do eiusmod tempor incid.</p>
  <div class="footer-col" style="left:432px">
    <h5>Home</h5>
    <ul><li>About Go</li><li>Services</li><li>Projects</li><li>Meet Team</li><li>Contact Us</li></ul>
  </div>
  <div class="footer-col" style="left:574px">
    <h5>Links</h5>
    <ul><li>Live Assets Works</li><li>Service Relocation</li><li>Compliance Testing</li><li>Our People</li></ul>
  </div>
  <div class="footer-col" style="left:768px"><h5>Contact</h5></div>
  <div class="contact-row" style="top:131px">
    <span class="icon"><svg width="16" height="18" viewBox="0 0 16 18"><path d="M8 1a6 6 0 0 0-6 6c0 4.5 6 10 6 10s6-5.5 6-10a6 6 0 0 0-6-6z" fill="#fff"/><circle cx="8" cy="7" r="2.3" fill="#0a9ddc"/></svg></span>
    <span>Address: Local name 123<br>Street name 123 Company.</span>
  </div>
  <div class="contact-row" style="top:180px;align-items:center">
    <span class="icon"><svg width="18" height="13" viewBox="0 0 18 13"><rect width="18" height="13" rx="1" fill="#fff"/><path d="M1 1l8 6 8-6" fill="none" stroke="#0a9ddc" stroke-width="1.6"/></svg></span>
    <span>Email: info@ridgelinehaul.com</span>
  </div>
  <div class="contact-row" style="top:231px;align-items:center">
    <span class="icon"><svg width="16" height="16" viewBox="0 0 16 16"><path d="M3 1l3 3-1.5 2a8 8 0 0 0 5.5 5.5l2-1.5 3 3-2 2C7 15 1 9 1 3z" fill="#fff"/></svg></span>
    <span>Phone: 555 014 2298</span>
  </div>
  <div class="footer-rule"></div>
  <p class="copyright">Copyrights © 2023 All rights reserved.</p>
</footer>

</body>
</html>
```